Fun Language School in San Diego, CA - We want cool Business Card

We need a new business card design for our new logo. We are a language school in beautiful San Diego, California. Our target is students from all over the world who age from 18 to 25. They come to our school to learn English. Our school has a modern look, trending and fun place. We are the only language school who use tablets in class. We are student oriented, Students Come First is our slogan. We are re-branding ourselves with a new logo. We would like to see a designs that use our new logo and it should reflect the feel of young, fun, modern, high-tech and attractive to young people.
I've seen some business card designs with transparent look, unusual shapes, we are open to any cool ideas. Thank you very much!

In order for you to know more about our school, here are the links to our Youtube Channel and Facebook.

Youtube: https://www.vidmarlo.example/channel/ZXpolrT-48kwb2nH7c5DqLm
Facebook: https://www.friendlane.example/BVSchool

Target Market(s)

Our target is students from all over the world who age from 18 to 25. International students.

Industry/Entity Type

School

Font styles to use
Sans Serif

Requirements
Must have
• Our new logo. Name, title and address.
Should not have
• Other colors other than the ones we have in our logo. Characters are fine.

```html
<!DOCTYPE html>
<html lang="en">
<head>
<meta charset="utf-8">
<title>BV School – Business Card</title>
<link href="https://fonts.googleapis.com/css2?family=Arimo:wght@400;700&display=swap" rel="stylesheet">
<style>
  :root {
    --backdrop: #e9e9ea;
    --card: #121315;
    --ink: #ffffff;
    --brand-teal: #0aa3ad;
    --card-shadow: rgba(0, 0, 0, 0.35);
  }
  * { box-sizing: border-box; margin: 0; padding: 0; }
  html, body {
    width: 1200px;
    height: 1000px;
    overflow: hidden;
    background: var(--backdrop);
    font-family: "Arimo", Arial, sans-serif;
    color: var(--ink);
  }
  .canvas {
    position: relative;
    width: 1200px;
    height: 1000px;
  }
  .business-card {
    position: absolute;
    left: 380px;
    top: 126px;
    width: 440px;
    height: 748px;
    background: var(--card);
    border-top-left-radius: 82px;
    box-shadow: 0 6px 14px var(--card-shadow);
  }
  .brand {
    position: absolute;
    left: 22px;
    top: 40px;
    display: flex;
    align-items: center;
    gap: 16px;
  }
  .brand-dot {
    width: 60px;
    height: 60px;
    border-radius: 50%;
    background: var(--brand-teal);
  }
  .brand-name {
    font-size: 44px;
    font-weight: 400;
    letter-spacing: 0.5px;
    color: var(--ink);
  }
  .identity {
    position: absolute;
    left: 0;
    right: 0;
    top: 340px;
    text-align: center;
  }
  .person-name {
    font-size: 24px;
    font-weight: 400;
    line-height: 30px;
  }
  .person-name strong { font-weight: 700; }
  .person-title {
    font-size: 20px;
    line-height: 28px;
  }
  .contact {
    position: absolute;
    left: 0;
    right: 0;
    top: 548px;
    text-align: center;
    font-size: 20.5px;
    line-height: 29px;
    font-style: normal;
  }
  .contact p + p { margin-top: 17px; }
  .contact .fax { margin-top: 0; }
  .contact .email { margin-top: 14px; }
</style>
</head>
<body>
<main class="canvas">
  <article class="business-card">
    <header class="brand">
      <span class="brand-dot" aria-hidden="true"></span>
      <span class="brand-name">BV School</span>
    </header>

    <section class="identity">
      <h1 class="person-name">Marlow <strong>Keane</strong></h1>
      <p class="person-title">Principle</p>
    </section>

    <address class="contact">
      <p>2740 Harbor Row, Ste 210<br>San Diego, CA 92101</p>
      <p>P: &nbsp;+1.619.555.0148<br><span class="fax">F: &nbsp;619.555.0193</span></p>
      <p class="email">E: &nbsp;hello@bvschool.example</p>
    </address>
  </article>
</main>
</body>
</html>
```